Business card design for Tolvin Waste

I would like double-sided business cards for myself and my partner that includes our logo and the existing colour scheme. We provide waste and environmental services to customers in the motor-vehicle and engineering industries.

```html
<!DOCTYPE html>
<html lang="en">
<head>
<meta charset="utf-8">
<title>Tolvin Waste – Business Card</title>
<link rel="stylesheet" href="https://fonts.googleapis.com/css2?family=Montserrat:wght@600&family=Roboto:wght@400;500&display=swap">
<style>
  :root {
    --page-bg: #f4f5f3;
    --card-white: #ffffff;
    --card-grey: #ececec;
    --ink: #555a5e;
    --ink-dark: #4a4f53;
    --green: #7cbf2e;
    --green-light: #a6d63a;
    --green-deep: #4ea63c;
    --wave-grey: #d9d9d9;
  }
  * { box-sizing: border-box; margin: 0; padding: 0; }
  html, body { width: 1200px; height: 900px; overflow: hidden; }
  body {
    background: var(--page-bg);
    font-family: "Roboto", Arial, sans-serif;
    position: relative;
  }
  .card {
    position: absolute;
    top: 300px;
    width: 520px;
    height: 300px;
    border-radius: 22px;
    overflow: hidden;
    box-shadow: 0 14px 30px rgba(0,0,0,0.12);
  }
  .card--front { left: 60px; background: linear-gradient(135deg, var(--card-white) 0%, var(--card-grey) 100%); }
  .card--back  { left: 620px; background: linear-gradient(135deg, var(--green-light) 0%, var(--green) 50%, var(--green-deep) 100%); }

  .card__texture { position: absolute; inset: 0; }

  .brand {
    position: absolute;
    display: flex;
    align-items: center;
    gap: 12px;
    font-family: "Montserrat", Arial, sans-serif;
    font-weight: 600;
    text-transform: uppercase;
    letter-spacing: 2px;
  }
  .brand__dot { border-radius: 50%; flex: none; }
  .card--front .brand { left: 24px; top: 44px; font-size: 30px; color: var(--ink-dark); }
  .card--front .brand__dot { width: 46px; height: 46px; border: 4px solid var(--green); }
  .card--back .brand { left: 50%; top: 50%; transform: translate(-50%, -50%); font-size: 36px; color: #ffffff; white-space: nowrap; }
  .card--back .brand__dot { width: 58px; height: 58px; border: 4px solid #ffffff; }

  .contact { position: absolute; left: 22px; top: 138px; list-style: none; font-size: 12px; color: var(--ink); }
  .contact li { display: flex; align-items: flex-start; gap: 8px; margin-bottom: 9px; line-height: 1.3; }
  .contact svg { width: 13px; height: 13px; flex: none; margin-top: 1px; }

  .holder { position: absolute; right: 34px; top: 150px; text-align: right; }
  .holder__name { font-size: 17px; font-weight: 500; color: var(--green); }
  .holder__role { font-size: 13px; color: var(--ink); margin-top: 8px; }

  .card__waves { position: absolute; left: 0; bottom: 0; width: 520px; height: 100px; }
</style>
</head>
<body>

  <section class="card card--front" aria-label="Business card front">
    <div class="card__texture" role="img" aria-label="Soft grey low-poly texture"></div>

    <div class="brand"><span class="brand__dot"></span>Tolvin Waste</div>

    <ul class="contact">
      <li>
        <svg viewBox="0 0 14 14"><circle cx="7" cy="7" r="7" fill="var(--green)"/><path d="M4.5 3.8l1.4-.3.7 1.7-.9.7c.5 1 1.2 1.7 2.2 2.2l.7-.9 1.7.7-.3 1.4c-3 0-5.5-2.5-5.5-5.5z" fill="#fff"/></svg>
        0861 72 31 48
      </li>
      <li>
        <svg viewBox="0 0 14 14"><circle cx="7" cy="7" r="7" fill="var(--green)"/><rect x="3.5" y="4.5" width="7" height="5" rx=".6" fill="#fff"/><path d="M3.7 4.8L7 7.3l3.3-2.5" stroke="var(--green)" stroke-width=".8" fill="none"/></svg>
        info@tolvinwaste.com
      </li>
      <li>
        <svg viewBox="0 0 14 14"><circle cx="7" cy="7" r="7" fill="var(--green)"/><circle cx="7" cy="7" r="3.6" stroke="#fff" stroke-width=".9" fill="none"/><path d="M3.4 7h7.2M7 3.4c-1.6 2-1.6 5.2 0 7.2M7 3.4c1.6 2 1.6 5.2 0 7.2" stroke="#fff" stroke-width=".8" fill="none"/></svg>
        www.tolvinwaste.com
      </li>
      <li>
        <svg viewBox="0 0 14 14"><circle cx="7" cy="7" r="7" fill="var(--green)"/><path d="M7 11S4.2 7.9 4.2 6A2.8 2.8 0 0 1 9.8 6C9.8 7.9 7 11 7 11z" fill="#fff"/><circle cx="7" cy="6" r="1" fill="var(--green)"/></svg>
        <span>No. 41207, birchway lane<br>fairmont vale 318</span>
      </li>
    </ul>

    <div class="holder">
      <p class="holder__name">Marlow Pettigrew</p>
      <p class="holder__role">Manager</p>
    </div>

    <svg class="card__waves" viewBox="0 0 520 100" preserveAspectRatio="none" aria-hidden="true">
      <path d="M0 62 C120 40 200 95 330 70 C420 52 480 20 520 8 L520 30 C470 45 420 78 330 88 C210 102 120 60 0 80 Z" fill="var(--wave-grey)"/>
      <path d="M0 56 C140 60 230 85 340 55 C420 34 480 18 520 4 L520 18 C480 34 420 58 340 72 C230 92 140 66 0 66 Z" fill="var(--green-light)"/>
      <path d="M180 84 C280 74 390 40 520 28 L520 44 C400 52 300 84 200 92 Z" fill="var(--green)"/>
      <path d="M0 84 C100 70 170 98 260 94 C200 100 100 100 0 96 Z" fill="var(--wave-grey)"/>
    </svg>
  </section>

  <section class="card card--back" aria-label="Business card back">
    <div class="card__texture" role="img" aria-label="Green low-poly texture"></div>
    <div class="brand"><span class="brand__dot"></span>Tolvin Waste</div>
  </section>

</body>
</html>
```